Business Card Design Project

I need a business card design for our new logo, please check the logo at the following link:
https://www.boxtrove.net/s/k7pqwe93mz41xr/TulipCrew.png
The address on the business card:
Av. Orlândio Vasconte 418 sala 207
Barra da Tijuca, Rio de Janeiro, RJ
CEP: 22719-480
Brasil
Phone: +55 21 74302186
e-mail: renato@tulipcrew.com.br
Updates
Thank you all for sending your designs, we will not provide feedback because there are too many designs, on December 3 we will pick the best design according to our point of view. Please keep posting.
Renato

```html
<!DOCTYPE html>
<html lang="pt-BR">
<head>
<meta charset="UTF-8">
<title>TulipCrew – Business Card</title>
<link rel="stylesheet" href="https://fonts.googleapis.com/css2?family=Oswald:wght@500;700&family=Pathway+Gothic+One&display=swap">
<style>
  :root {
    --canvas-bg: #dfe3e6;
    --card-yellow: #f7c600;
    --card-white: #ffffff;
    --ink: #2a2a2a;
    --accent: #f7c600;
    --paper-shadow: rgba(0, 0, 0, 0.18);
  }
  * { margin: 0; padding: 0; box-sizing: border-box; }
  html, body {
    width: 1200px;
    height: 960px;
    overflow: hidden;
    background: var(--canvas-bg);
  }
  .canvas {
    width: 1200px;
    height: 960px;
    display: flex;
    flex-direction: column;
    align-items: center;
    justify-content: center;
    gap: 56px;
  }
  .card {
    position: relative;
    width: 760px;
    height: 420px;
    overflow: hidden;
    box-shadow: 0 10px 28px var(--paper-shadow);
  }

  /* Front side */
  .card--front { background: var(--card-yellow); color: var(--ink); }
  .name-band {
    position: absolute;
    left: 0; top: 52px;
    width: 420px; height: 56px;
    background: var(--ink);
    display: flex;
    align-items: center;
    padding-left: 90px;
  }
  .name {
    font-family: "Oswald", sans-serif;
    font-weight: 500;
    font-size: 31px;
    letter-spacing: 2px;
    color: #ffffff;
    text-transform: uppercase;
  }
  .role {
    position: absolute;
    left: 90px; top: 124px;
    font-family: "Pathway Gothic One", sans-serif;
    font-size: 23px;
    letter-spacing: 0.5px;
  }
  .contact-list {
    position: absolute;
    left: 40px; top: 186px;
    list-style: none;
    font-family: "Pathway Gothic One", sans-serif;
    font-size: 22px;
    letter-spacing: 0.8px;
    line-height: 1.3;
  }
  .contact-item {
    display: flex;
    align-items: flex-start;
    gap: 22px;
    margin-bottom: 18px;
  }
  .contact-icon {
    flex: none;
    width: 30px; height: 30px;
  }
  .illustration--runner {
    position: absolute;
    left: 490px; top: 60px;
    width: 270px; height: 290px;
    background: radial-gradient(ellipse at 55% 50%, #3a3a3a 0%, #2a2a2a 55%, rgba(42,42,42,0) 72%);
  }

  /* Back side */
  .card--back { background: var(--card-white); }
  .illustration--mascot {
    position: absolute;
    left: 250px; top: 52px;
    width: 290px; height: 170px;
    background: radial-gradient(ellipse at 50% 50%, #3a3a3a 0%, #2a2a2a 45%, rgba(247,198,0,0.5) 62%, rgba(255,255,255,0) 74%);
  }
  .brand-name {
    position: absolute;
    left: 150px; top: 222px;
    font-family: "Oswald", sans-serif;
    font-weight: 700;
    font-size: 76px;
    letter-spacing: 2px;
    color: var(--ink);
  }
  .brand-rule {
    position: absolute;
    left: 520px; top: 315px;
    width: 240px; height: 6px;
    background: var(--accent);
  }
</style>
</head>
<body>
<main class="canvas">

  <section class="card card--front" aria-label="Business card front">
    <div class="name-band"><h1 class="name">Luana Moretti</h1></div>
    <p class="role">Operation manager</p>

    <ul class="contact-list">
      <li class="contact-item">
        <svg class="contact-icon" viewBox="0 0 30 30" aria-hidden="true">
          <circle cx="15" cy="15" r="15" fill="#2a2a2a"/>
          <path d="M10 8.5c.6-.6 1.5-.5 2 .1l1.6 2c.4.5.4 1.2 0 1.7l-1 1c.8 1.7 2.2 3.1 3.9 3.9l1-1c.5-.4 1.2-.4 1.7 0l2 1.6c.6.5.7 1.4.1 2l-1 1c-1 1-2.6 1.2-3.9.5-3-1.6-5.5-4.1-7.1-7.1-.7-1.3-.5-2.9.5-3.9z" fill="#f7c600"/>
        </svg>
        <span>+55 21 74302186</span>
      </li>
      <li class="contact-item">
        <svg class="contact-icon" viewBox="0 0 30 30" aria-hidden="true">
          <circle cx="15" cy="15" r="15" fill="#2a2a2a"/>
          <rect x="8" y="10" width="14" height="10" rx="1" fill="#f7c600"/>
          <path d="M8.5 10.5 15 15.5l6.5-5" fill="none" stroke="#2a2a2a" stroke-width="1.4"/>
        </svg>
        <span>renato@tulipcrew.com.br</span>
      </li>
      <li class="contact-item">
        <svg class="contact-icon" viewBox="0 0 30 30" aria-hidden="true">
          <circle cx="15" cy="15" r="15" fill="#2a2a2a"/>
          <path d="M15 7a5.5 5.5 0 0 0-5.5 5.5c0 4 5.5 10 5.5 10s5.5-6 5.5-10A5.5 5.5 0 0 0 15 7z" fill="#f7c600"/>
          <circle cx="15" cy="12.5" r="2" fill="#2a2a2a"/>
        </svg>
        <address style="font-style: normal;">
          Av. Orlândio Vasconte 418 sala 207<br>
          Barra da Tijuca, Rio de Janeiro, RJ<br>
          CEP: 22719-480<br>
          Brasil
        </address>
      </li>
    </ul>

    <div class="illustration--runner" role="img" aria-label="Dark silhouette mascot illustration of the brand character running"></div>
  </section>

  <section class="card card--back" aria-label="Business card back">
    <div class="illustration--mascot" role="img" aria-label="Brand mascot illustration in dark grey with yellow accents"></div>
    <p class="brand-name">TulipCrew</p>
    <div class="brand-rule"></div>
  </section>

</main>
</body>
</html>
```